Three Fold Brochure for A Creative and Playful Mental Health Therapist

I need a brochure for myself, a mental health therapist and Registered Play Therapist in Marietta, Georgia. I serve women and children. I'd like to see designs with the colors dark teal and white, and with a butterfly or butterflies included somewhere in the brochure, and maybe vines or branches. I like traditional designs and fonts with serifs. I'd like a section about just me with copy about me and my headshot.

I'd also like one section to be for just women (looking for a therapist), and one section for just children, or children and parents. I need a section to include a description of Play Therapy, preferably the section focused on children. I'm attaching copywriting that can be used (but will need shortened). The highlighted areas are the most important. I need our group practice logo included somewhere small on the brochure. (This is information about just me, not our group practice.)

I'm uploading more pictures than needed because I can't decide which ones I want: feel free to chose the ones you think work best..

I'm also including pictures of my business cards, front and back, which I designed myself. I'm looking for a similar (but better) look for my brochure.

It needs to state somewhere that I am an Out of Network Provider and do not accept insurance.
Hours:Monday-Thursday 12:00 pm to 8;00 pm

Me: Carla Whitmore, MSW, LCSW, RPT
Company Name: Pine Hollow Wellness Center
Tag line: Helping women and children find lasting calm, confidence, direction, and healing.

Include address and phone number and email.

Pine Hollow Wellness Center
4175 Brindle Ave. Ste C310
Marietta, GA 30418
470-316-5082
carla@pinehollowwellnesscenter.example

Target Market(s)

Women and parents needing a therapist, and professionals recommending me

Industry/Entity Type

Mental Health Therapy

Font styles to use
Serif

Colors
0094D4
00A9DD
6FCCEA
C7EBF8
E9F6FB

Requirements
Must have
• A butterfly or a few, Dark Teal and White, A section about me, a section for women, and a section for parents and children
Nice to have
• Dark blue or medium blue (maybe the butterfly?)
Should not have
• Anything cartoon like or juvenile

```html
<!DOCTYPE html>
<html lang="en">
<head>
<meta charset="utf-8">
<title>Carla Whitmore Trifold Brochure</title>
<link href="https://fonts.googleapis.com/css2?family=Playfair+Display:wght@700;800&family=Lora:ital,wght@0,400;0,600;1,400&display=swap" rel="stylesheet">
<style>
:root{
  --teal:#2e4d53;
  --teal-line:rgba(255,255,255,.16);
  --orange:#e8772e;
  --gold:#f0a63a;
  --white:#ffffff;
  --paper:#fbfaf7;
  --ink:#33484c;
  --muted:#6b7d80;
  --stage:#d6d8d8;
  --photo-warm:#c9a48c;
  --photo-cool:#8fa7ad;
  --leaf-soft:rgba(232,119,46,.22);
}
*{box-sizing:border-box;margin:0;padding:0}
html,body{width:1200px;height:2604px;overflow:hidden}
body{background:var(--stage);font-family:"Lora",Georgia,serif;color:var(--ink);position:relative}
.sprite{position:absolute;width:0;height:0}
.spread{position:absolute;left:50px;width:1100px;height:830px;display:flex;box-shadow:0 10px 30px rgba(0,0,0,.18);background:var(--paper)}
.spread-outside{top:422px}
.spread-inside{top:1352px}
.panel{position:relative;width:366.67px;height:100%;padding:34px 30px 0;display:flex;flex-direction:column;overflow:hidden}
.panel + .panel{border-left:1px solid #e6e4de}
.heading{font-family:"Playfair Display",Georgia,serif;font-weight:800;font-size:18px;text-transform:uppercase;color:var(--teal);line-height:1.18;position:relative;z-index:1}
.heading .accent{color:var(--orange)}
.body-copy{font-size:11.5px;line-height:1.6;color:var(--ink);margin-top:10px;position:relative;z-index:1}
.leaf-art{position:absolute;z-index:0;border-radius:6px;background:linear-gradient(150deg,var(--leaf-soft),rgba(240,166,58,0))}
.wing-art{position:absolute;z-index:2;width:46px;height:34px;border-radius:8px;background:linear-gradient(135deg,rgba(232,119,46,.55),rgba(240,166,58,.25))}
.check-box{flex:1;display:flex;flex-direction:column;background:var(--teal);color:var(--white);padding:12px 20px;margin-top:16px;margin-bottom:30px}
.check-list{list-style:none;flex:1;display:flex;flex-direction:column;justify-content:space-around}
.check-list li{display:flex;align-items:center;gap:12px;font-size:11.5px;line-height:1.35;padding:6px 0;border-bottom:1px solid var(--teal-line)}
.check-list li:last-child{border-bottom:none}
.tick{flex:0 0 20px;width:20px;height:20px}
.photo{background:linear-gradient(160deg,var(--photo-cool),var(--photo-warm))}
.photo-bleed{margin-left:-30px;margin-right:-30px}
.photo-round{border-radius:50%;border:5px solid var(--white);box-shadow:0 0 0 3px var(--orange)}
.name-title{font-family:"Playfair Display",Georgia,serif;font-weight:800;font-size:20px;color:var(--teal);text-transform:uppercase;text-align:center;line-height:1.2}
.quote{font-style:italic;font-size:12px;text-align:center;color:var(--orange);margin:16px 0 8px;line-height:1.5}
.contact{text-align:center;font-size:12px;line-height:1.75;color:var(--ink)}
.contact strong{color:var(--teal);font-size:15px}
.web-bar{background:var(--teal);color:var(--white);text-align:center;font-size:12px;padding:12px 0;letter-spacing:.5px;margin:0 -30px}
.logo-block{display:flex;align-items:center;gap:12px;justify-content:flex-end}
.logo-square{width:16px;height:16px;background:var(--teal)}
.logo-name{font-family:"Playfair Display",Georgia,serif;font-weight:800;font-size:30px;color:var(--teal);letter-spacing:2px}
.logo-sub{font-size:9px;color:var(--muted);text-align:right;text-transform:uppercase;letter-spacing:1px;margin-top:2px}
.cover-band{display:flex;justify-content:center;gap:10px;background:var(--orange);color:var(--white);font-family:"Playfair Display",Georgia,serif;font-weight:800;font-size:22px;text-transform:uppercase;padding:10px 0;margin:0 -30px}
.cover-band .divider{color:var(--teal)}
.cover-tag{font-family:"Playfair Display",Georgia,serif;font-size:24px;color:var(--teal);text-align:center;margin-top:18px;font-weight:700}
.cover-values{font-size:12px;text-align:center;color:var(--orange);margin-top:6px;letter-spacing:.5px}
.small-note{font-size:11px;text-align:center;color:var(--muted);line-height:1.55;margin-top:14px}
.icon-list{list-style:none;margin-top:14px}
.icon-list li{display:flex;gap:12px;align-items:center;font-size:11.5px;line-height:1.4;margin-bottom:10px}
.dot-icon{flex:0 0 24px;width:24px;height:24px}
.therapist-panel{background:var(--teal);color:var(--white)}
.therapist-panel .name-title{color:var(--white);text-align:left}
.tag{align-self:flex-start;background:var(--orange);color:var(--white);font-family:"Playfair Display",Georgia,serif;font-weight:700;font-size:15px;text-transform:uppercase;padding:5px 14px;margin:10px 0 6px;letter-spacing:1px}
.therapist-panel .body-copy{color:#e6eeee}
.hours-line{margin-top:auto;margin-bottom:28px;padding-top:12px;border-top:1px solid var(--teal-line);font-size:11.5px;color:var(--gold);line-height:1.6}
</style>
</head>
<body>

<svg class="sprite" aria-hidden="true">
  <symbol id="tick-mark" viewBox="0 0 20 20"><circle cx="10" cy="10" r="9" fill="none" stroke="#fff" stroke-width="1.5"/><path d="M6 10.5l3 3 5-6" fill="none" stroke="#f0a63a" stroke-width="2"/></symbol>
  <symbol id="teal-tick" viewBox="0 0 24 24"><circle cx="12" cy="12" r="12" fill="#2e4d53"/><path d="M7 12.5l3.2 3.2 6.3-7" fill="none" stroke="#f0a63a" stroke-width="2.2"/></symbol>
</svg>

<!-- Outside spread -->
<section class="spread spread-outside">
  <article class="panel">
    <div class="leaf-art" style="left:0;top:0;width:70px;height:190px" role="img" aria-label="Autumn vine with leaves along the corner"></div>
    <h2 class="heading" style="font-size:19px">Children and teens struggling with <span class="accent">aggression, anxiety, and impulsive behaviors</span></h2>
    <p class="body-copy">Play therapy gives children a safe, natural way to express big feelings. Through toys, art and guided play, your child learns new skills to calm down, cope with worry and make better choices at home and school.</p>
    <div class="check-box">
      <ul class="check-list">
        <li><svg class="tick"><use href="#tick-mark"/></svg>Hitting, Kicking, Throwing Things</li>
        <li><svg class="tick"><use href="#tick-mark"/></svg>Refusing to Comply with Adults</li>
        <li><svg class="tick"><use href="#tick-mark"/></svg>Explosive Temper Tantrums</li>
        <li><svg class="tick"><use href="#tick-mark"/></svg>Worrying or Being Clingy</li>
        <li><svg class="tick"><use href="#tick-mark"/></svg>Trouble Sleeping at Night</li>
        <li><svg class="tick"><use href="#tick-mark"/></svg>Difficulty Focusing and Listening</li>
        <li><svg class="tick"><use href="#tick-mark"/></svg>Acting Without Thinking First</li>
        <li><svg class="tick"><use href="#tick-mark"/></svg>Frequent Arguments or Defiance</li>
        <li><svg class="tick"><use href="#tick-mark"/></svg>Low Frustration Tolerance</li>
        <li><svg class="tick"><use href="#tick-mark"/></svg>Difficulty Naming Feelings</li>
        <li><svg class="tick"><use href="#tick-mark"/></svg>Struggling with Friendships</li>
      </ul>
    </div>
  </article>

  <article class="panel">
    <h2 class="name-title">Carla Whitmore,<br>MSW, LCSW, RPT</h2>
    <div class="photo photo-round" style="width:150px;height:150px;margin:16px auto 0;flex:0 0 150px" role="img" aria-label="Headshot of Carla Whitmore"></div>
    <div class="wing-art" style="right:52px;top:190px" role="img" aria-label="Blue and orange butterfly illustration"></div>
    <p class="quote">“Helping women and children find lasting calm, confidence, direction, and healing.”</p>
    <p class="small-note" style="margin-top:0">Out of Network Provider. Insurance is not accepted; receipts provided for reimbursement.<br>Hours: Monday–Thursday, 12:00 pm to 8:00 pm</p>
    <div class="contact" style="margin-top:14px">
      <strong>470-316-5082</strong><br>
      carla@pinehollowwellnesscenter.example<br>
      Pine Hollow Wellness Center<br>
      4175 Brindle Ave. Ste C310, Marietta, GA 30418
    </div>
    <div class="photo photo-bleed" style="margin-top:auto;height:190px" role="img" aria-label="Photo of a group of smiling children sitting together"></div>
    <div class="web-bar">www.pinehollowwellnesscenter.example</div>
  </article>

  <article class="panel" style="padding-top:28px">
    <div class="logo-block">
      <span class="logo-square"></span>
      <span class="logo-name">PHWC</span>
    </div>
    <p class="logo-sub">Pine Hollow Wellness Center</p>
    <div class="photo photo-bleed" style="height:380px;margin-top:16px" role="img" aria-label="Photo of a smiling mother and daughter outdoors"></div>
    <div class="cover-band"><span>Women</span><span class="divider">|</span><span>Children</span></div>
    <p class="cover-tag">Find Lasting</p>
    <p class="cover-values">Calm • Confidence • Direction • Healing</p>
    <p class="small-note">Therapy and play therapy for women, children, teens and parents in a warm, welcoming setting in Marietta, Georgia.</p>
    <p class="small-note" style="margin-top:8px">Carla Whitmore, MSW, LCSW, RPT · 470-316-5082</p>
    <div class="leaf-art" style="right:0;bottom:0;width:130px;height:110px;background:linear-gradient(330deg,var(--leaf-soft),rgba(240,166,58,0))" role="img" aria-label="Autumn branch with leaves in the corner"></div>
    <div class="wing-art" style="left:36px;bottom:34px" role="img" aria-label="Butterfly illustration"></div>
  </article>
</section>

<!-- Inside spread -->
<section class="spread spread-inside">
  <article class="panel">
    <div class="leaf-art" style="left:0;top:0;width:70px;height:160px" role="img" aria-label="Autumn vine with leaves along the corner"></div>
    <h2 class="heading">Parents of an <span class="accent">aggressive, impulsive, and/or anxious</span> child or teen</h2>
    <p class="body-copy">Parenting a struggling child can leave you exhausted and unsure. Together we build tools that bring peace back home and help you feel confident again.</p>
    <ul class="icon-list" style="flex:1;display:flex;flex-direction:column;justify-content:space-around;margin-bottom:10px">
      <li><svg class="dot-icon"><use href="#teal-tick"/></svg>You feel frustrated and helpless when parenting</li>
      <li><svg class="dot-icon"><use href="#teal-tick"/></svg>Your bond with your child feels strained</li>
      <li><svg class="dot-icon"><use href="#teal-tick"/></svg>You worry about how others see your child</li>
      <li><svg class="dot-icon"><use href="#teal-tick"/></svg>Discipline no longer seems to work</li>
      <li><svg class="dot-icon"><use href="#teal-tick"/></svg>Calls from school are becoming routine</li>
      <li><svg class="dot-icon"><use href="#teal-tick"/></svg>You want a calmer, happier home</li>
      <li><svg class="dot-icon"><use href="#teal-tick"/></svg>You need support you can trust</li>
    </ul>
    <div class="photo photo-bleed" style="height:230px;flex:0 0 230px" role="img" aria-label="Photo of a family sitting together"></div>
  </article>

  <article class="panel">
    <h2 class="heading">Women feeling <span class="accent">stuck, overwhelmed, anxious,</span> and/or ashamed of the past</h2>
    <p class="body-copy">Life can pile up until it feels too heavy to carry alone. You deserve a space that is just for you.</p>
    <ul class="icon-list">
      <li><svg class="dot-icon"><use href="#teal-tick"/></svg>You feel stuck and unsure of your next step</li>
      <li><svg class="dot-icon"><use href="#teal-tick"/></svg>Your mind races and rest feels out of reach</li>
      <li><svg class="dot-icon"><use href="#teal-tick"/></svg>You put everyone else first, every time</li>
      <li><svg class="dot-icon"><use href="#teal-tick"/></svg>Past hurts still shape how you see yourself</li>
      <li><svg class="dot-icon"><use href="#teal-tick"/></svg>You feel disconnected, lonely or numb</li>
      <li><svg class="dot-icon"><use href="#teal-tick"/></svg>You are ready to feel like yourself again</li>
    </ul>
    <div class="photo photo-bleed" style="height:220px;flex:0 0 220px;margin-top:6px" role="img" aria-label="Photo of two women talking and smiling"></div>
    <p class="body-copy" style="margin-top:14px">Let's work together to find lasting calm and renewed confidence, so you can move forward with clear direction and a sense of healing.</p>
    <p class="body-copy">Sessions are gentle, practical and paced for you, with tools you can use right away in daily life.</p>
    <div class="wing-art" style="right:30px;bottom:24px" role="img" aria-label="Butterfly illustration"></div>
  </article>

  <article class="panel therapist-panel">
    <div class="photo photo-bleed" style="height:270px;flex:0 0 270px;margin-top:-34px;margin-bottom:18px" role="img" aria-label="Portrait of Carla Whitmore"></div>
    <div class="wing-art" style="right:30px;top:250px" role="img" aria-label="Butterfly illustration"></div>
    <h2 class="name-title">Carla Whitmore,<br>MSW, LCSW, RPT</h2>
    <span class="tag">Meet the Therapist</span>
    <p class="body-copy">I am a Licensed Clinical Social Worker and Registered Play Therapist in Marietta, Georgia. I help women and children heal, grow and build lasting confidence.</p>
    <p class="body-copy">With children, I use play, the natural language of kids, to help them share feelings and learn new skills. With women, I offer a calm space to untangle stress and find direction.</p>
    <p class="body-copy">I am an Out of Network Provider and do not accept insurance. Receipts are provided for reimbursement.</p>
    <p class="hours-line">Hours: Monday–Thursday, 12:00 pm to 8:00 pm<br>470-316-5082 · Marietta, GA 30418</p>
  </article>
</section>

</body>
</html>
```